Building Servicess

We need a new business card design for a company. We specialise in: Electrical/Site temporary electrics, Data/Network Installation, Passive Fire Protection

Industry/Entity Type

Construction

Contact Information for Business Card

Services provided as detailed on project description

Font styles to use
Serif

Colors
0054AA
0677BA
7BADD7
CADEEF
E8F1F8
00AB8E
00BBA5
67D7C9
C6EFE9
E9F9F6
EB3D1F
EC4F4E
F09395
F8D3D4
FCEDEE

Requirements
Must have
• Company logo-contact details-phone numbers

```html
<!DOCTYPE html>
<html lang="en">
<head>
<meta charset="utf-8">
<title>Norvale Services Ltd – Business Card</title>
<link href="https://fonts.googleapis.com/css2?family=Arimo:wght@400;700&display=swap" rel="stylesheet">
<style>
  :root {
    --backdrop: #eef0f3;
    --card: #ffffff;
    --brand-blue: #1f6fc0;
    --icon-blue: #2a7fc9;
    --text-grey: #85888d;
    --photo-light: #4b8fd6;
    --photo-mid: #1f5fb0;
    --photo-dark: #0c2f78;
    --card-shadow: rgba(40, 50, 70, 0.18);
  }
  * { margin: 0; padding: 0; box-sizing: border-box; }
  html, body {
    width: 1200px;
    height: 800px;
    overflow: hidden;
    background: var(--backdrop);
    font-family: "Arimo", Arial, sans-serif;
  }
  .canvas {
    position: relative;
    width: 1200px;
    height: 800px;
  }
  .card {
    position: absolute;
    top: 232px;
    width: 520px;
    height: 336px;
    background: var(--card);
    box-shadow: 0 10px 30px var(--card-shadow);
    overflow: hidden;
  }
  .card--front { left: 60px; }
  .card--back  { left: 620px; }

  .card__photo {
    position: absolute;
    inset: 0;
    width: 520px;
    height: 336px;
  }
  .identity {
    position: absolute;
    left: 36px;
    top: 100px;
    text-transform: uppercase;
  }
  .identity__name {
    color: var(--brand-blue);
    font-weight: 700;
    font-size: 22px;
    letter-spacing: 0.2px;
  }
  .identity__role {
    color: var(--text-grey);
    font-size: 15px;
    margin-top: 3px;
  }
  .contacts {
    position: absolute;
    left: 32px;
    top: 210px;
    list-style: none;
  }
  .contacts__item {
    display: flex;
    align-items: center;
    gap: 10px;
    height: 36px;
    color: var(--text-grey);
    font-size: 15px;
  }
  .contacts__icon {
    width: 16px;
    height: 16px;
    flex: none;
  }
  .brand {
    position: absolute;
    inset: 0;
    display: flex;
    align-items: center;
    justify-content: center;
    gap: 12px;
  }
  .brand__square {
    width: 22px;
    height: 22px;
    background: var(--brand-blue);
  }
  .brand__name {
    color: var(--brand-blue);
    font-weight: 700;
    font-size: 28px;
    text-transform: uppercase;
    letter-spacing: 0.5px;
  }
</style>
</head>
<body>
<main class="canvas">
  <section class="card card--front">
    <svg class="card__photo" viewBox="0 0 520 336" role="img" aria-label="Blue-toned photograph of glass office tower facades">
      <defs>
        <linearGradient id="photoTone" x1="0" y1="0" x2="1" y2="1">
          <stop offset="0" stop-color="var(--photo-light)"/>
          <stop offset="0.5" stop-color="var(--photo-mid)"/>
          <stop offset="1" stop-color="var(--photo-dark)"/>
        </linearGradient>
      </defs>
      <polygon points="447,0 520,0 520,336 328,336 234,208" fill="url(#photoTone)"/>
    </svg>

    <div class="identity">
      <p class="identity__name">Marek Dalton</p>
      <p class="identity__role">Managing Director</p>
    </div>

    <ul class="contacts">
      <li class="contacts__item">
        <svg class="contacts__icon" viewBox="0 0 24 24" aria-hidden="true">
          <path fill="var(--icon-blue)" d="M6.6 10.8a15.1 15.1 0 0 0 6.6 6.6l2.2-2.2a1 1 0 0 1 1-.25 11.4 11.4 0 0 0 3.6.57 1 1 0 0 1 1 1V20a1 1 0 0 1-1 1A17 17 0 0 1 3 4a1 1 0 0 1 1-1h3.5a1 1 0 0 1 1 1 11.4 11.4 0 0 0 .57 3.6 1 1 0 0 1-.25 1z"/>
        </svg>
        <span>07700 900418</span>
      </li>
      <li class="contacts__item">
        <svg class="contacts__icon" viewBox="0 0 24 24" aria-hidden="true">
          <rect x="6" y="2" width="12" height="20" rx="2" fill="none" stroke="var(--icon-blue)" stroke-width="2.2"/>
          <circle cx="12" cy="18" r="1.3" fill="var(--icon-blue)"/>
        </svg>
        <span>020 7946 0321</span>
      </li>
      <li class="contacts__item">
        <svg class="contacts__icon" viewBox="0 0 24 24" aria-hidden="true">
          <circle cx="12" cy="12" r="10" fill="var(--icon-blue)"/>
          <path d="M2 12h20M12 2c3 3 3 17 0 20M12 2c-3 3-3 17 0 20" fill="none" stroke="#fff" stroke-width="1.4"/>
        </svg>
        <span>www.norvaleservices.co.uk</span>
      </li>
    </ul>
  </section>

  <section class="card card--back">
    <div class="brand">
      <span class="brand__square" aria-hidden="true"></span>
      <span class="brand__name">Norvale Services Ltd</span>
    </div>
  </section>
</main>
</body>
</html>
```